Tallowmere Office Solutions needs a new interactive and interesting website

We need an interesting, professional, modern and functional company website for Tallowmere Office Solutions - a young IT Services company based out of Chennai, India.

Tallowmere Office Solutions is a fully owned subsidiary of Hollin Cellarhouse, one of the world's leading direct to consumer wine merchant.

We already have a registered company logo which must feature in the website.

We conceive, design, develop, test, implement and support IT solutions across the entire Hollin Cellarhouse IT landscape. For ex : We currently run about 25 e-commerce websites for Hollin Cellarhouse on QVM and Dot Net.

We would like to see our corporate colors used in the website. (Burgundy wine and wine green - source: www.tallowmereos.example)

We are looking at this website to communicate a fun, friendly and professionally managed company - reaching out to career seekers, prospective customers and general public.

For reference - The company name 'Tallowmere' is an inspiration from the Hollin Cellarhouse lineage.

The second image with the world map is stickered on our main entrance to the office, I am not sure where this can be used -just putting it out there..
Updates

Please note that there are only a few more days to submit designs for this contest  !

I would appreciate if you can help posting your designs in time for our review and consideration.

Thanks.

Project Deadline Extended
Reason: Thanks for your inputs. We have a number of designers and a lot to digest and work with in the past few days. There has been a rush of new designs in the last few days Hence we will require more time to process these and make our decision. Hence i am requesting the contest to be open for more days. Regards, Soren

Target Market(s)

Prospective job seekers who want to know more about the company and also wish to apply for a job vacancy
People wanting to know more about the company in general and our progress
People who want to see what we offer and how we can help them too - prospective customers
Companies that are interested in our IT Captive journey and are looking for a business opportunity

Industry/Entity Type

E-Commerce

Requirements
Must have
• Log In/ Register facility acting as a Single Sign on for Intranet (Employees)

Facility to post job vacancies (with an expiry date) and enable people to apply for a role and upload their CV/Resume.

Facility to Review Job applications

Facility for website visitors to contact Tallowmere office Solutions via an online 'Contact Us' form with a split of job seekers and business opportunities

Gallery facility to upload pictures regarding company events
Nice to have
• Less Cluttered and contemporary design
Some Wine/Vineyard inspirations will be good but not too much, the company is an IT services company

```html
<!DOCTYPE html>
<html lang="en">
<head>
<meta charset="utf-8">
<title>Tallowmere Office Solutions</title>
<link href="https://fonts.googleapis.com/css2?family=Open+Sans:wght@400;600;700&family=Roboto+Condensed:wght@400;700&display=swap" rel="stylesheet">
<style>
:root{
  --wine:#8a0f45;
  --wine-dark:#5c0a2c;
  --wine-mid:#7a0d3c;
  --gold:#f5c21b;
  --text:#555;
  --heading:#2a2a2a;
  --panel:#f2f2f2;
  --tile:#eeeeee;
  --footer:#1e1e1e;
  --footer-bar:#111;
  --footer-text:#bdbdbd;
}
*{margin:0;padding:0;box-sizing:border-box}
html,body{width:760px;height:1200px;overflow:hidden;background:#fff}
body{position:relative;font-family:"Open Sans",Arial,sans-serif;color:var(--text)}
.abs{position:absolute}

/* header */
.masthead{left:0;top:0;width:760px;height:368px;
  background:radial-gradient(ellipse at 50% 10%,#9a1452 0%,var(--wine-mid) 45%,var(--wine-dark) 100%)}
.masthead-curve{left:0;top:0;width:760px;height:80px}
.brand{left:83px;top:17px;color:#fff;display:flex;align-items:center;gap:7px}
.brand-dot{width:24px;height:24px;border-radius:50%;background:#fff;opacity:.9}
.brand-name{font-size:22px;font-weight:700;line-height:22px;letter-spacing:-.5px}
.brand-sub{font-size:14px;font-weight:400;line-height:18px}
.phone-top{right:83px;top:11px;color:var(--gold);font-size:14px;display:flex;align-items:center;gap:6px}
.nav{left:280px;top:43px;width:397px;display:flex;justify-content:space-between;font-size:8.5px;font-weight:600;color:#fff;text-transform:uppercase;white-space:nowrap}
.nav a{color:#fff;text-decoration:none;position:relative}
.nav a.active:after{content:"";position:absolute;left:0;right:0;bottom:-6px;height:2px;background:var(--gold)}

.hero{left:83px;top:83px;width:594px;height:265px;border:5px solid #fff;border-radius:4px;
  background:
    radial-gradient(ellipse 35% 70% at 22% 45%,rgba(190,90,80,.85) 0%,rgba(190,90,80,0) 100%),
    radial-gradient(ellipse 30% 60% at 78% 55%,rgba(45,48,58,.9) 0%,rgba(45,48,58,0) 100%),
    linear-gradient(100deg,#9a6a4e 0%,#6f8a44 40%,#4f6a38 65%,#3a3f3a 100%);
  overflow:hidden}
.hero-title{left:272px;top:84px;color:#fff;font-family:"Roboto Condensed",sans-serif;font-weight:700;font-size:27px;line-height:30px;letter-spacing:1px;text-shadow:0 1px 3px rgba(0,0,0,.4)}
.hero-dots{left:17px;top:233px;display:flex;gap:4px}
.hero-dots span{width:8px;height:8px;border-radius:50%;border:1.5px solid #fff;background:rgba(0,0,0,.3)}
.hero-dots span.on{background:var(--gold)}

/* welcome */
.welcome{left:0;top:368px;width:760px;height:212px;background:linear-gradient(#fff 0%,#f1f1f1 100%)}
.grapes{left:112px;top:432px;width:80px;height:105px;border-radius:40% 40% 50% 50%;background:var(--wine);opacity:.85}
.welcome-title{left:224px;top:418px;font-family:"Roboto Condensed",sans-serif;font-size:18px;font-weight:400;color:var(--heading);white-space:nowrap}
.welcome-title b,.section-title b{color:var(--wine);font-weight:400}
.copy{font-size:8.3px;line-height:13.5px;color:#666}
.welcome-copy{left:224px;top:449px;width:456px}
.welcome-copy p+p{margin-top:13px}

/* services */
.services-tab{left:0;top:590px;width:215px;height:90px}
.section-title{left:83px;top:623px;font-family:"Roboto Condensed",sans-serif;font-size:18px;font-weight:400;color:var(--heading)}
.services-copy{left:224px;top:611px;width:456px}
.tile{width:221px;height:24px;background:var(--tile);font-family:"Roboto Condensed",sans-serif;font-size:10px;color:#666;line-height:24px;padding-left:8px;white-space:nowrap}
.tile:before{content:"» ";color:#888}

/* cards */
.card{top:787px;width:178px;height:209px;background:var(--panel);border-radius:0 0 6px 6px}
.card-head{height:36px;background:var(--wine);color:#fff;font-family:"Roboto Condensed",sans-serif;font-size:17px;line-height:36px;padding-left:8px;border-radius:0 14px 0 0}
.item{position:absolute;left:10px;width:160px}
.date{font-size:8px;color:#777;margin-left:2px}
.item-title{font-size:8.6px;font-weight:700;color:#222;line-height:12px}
.item-text{font-size:8px;color:#666;line-height:12px;margin-top:3px}
.more{color:var(--wine)}
.divider{position:absolute;left:8px;right:8px;height:1px;background:#ddd}
.thumb{position:absolute;left:8px;width:48px;height:48px;background:linear-gradient(135deg,#6b4a3a,#c9a58a);border-radius:2px}
.event{position:absolute;left:67px;width:105px}
.client-box{position:absolute;left:8px;top:80px;width:161px;height:75px;background:#fff;display:flex;align-items:center;justify-content:center;font-size:13px;font-weight:700;color:#222}
.client-link{position:absolute;left:0;right:0;top:162px;font-size:8.5px;color:var(--wine);display:flex;align-items:center;justify-content:center;gap:4px;white-space:nowrap}
.client-link i{width:8px;height:8px;border-radius:50%;background:#555;display:inline-block}
.arrows{position:absolute;left:73px;top:185px;display:flex;gap:3px}
.arrows span{width:13px;height:13px;border-radius:50%;background:#ddd;font-size:8px;line-height:13px;text-align:center;color:#555}

/* footer */
.footer{left:0;top:1026px;width:760px;height:149px;background:var(--footer)}
.foot-col h4{font-family:"Roboto Condensed",sans-serif;color:#fff;font-size:12px;font-weight:700;text-transform:uppercase;margin-bottom:8px}
.foot-col li{list-style:none;font-size:8px;line-height:14.3px;color:var(--footer-text)}
.foot-col .addr li{line-height:11.5px}
.foot-phone{font-size:12px;color:#fff;margin-top:10px}
.foot-mail{font-size:8px;color:var(--footer-text);line-height:12px}
.social{display:flex;align-items:center;gap:3px;margin-bottom:12px}
.social .btn{height:12px;padding:0 4px;background:#3b5b98;color:#fff;font-size:7px;line-height:12px;border-radius:2px;display:flex;align-items:center;gap:3px}
.social .btn i{width:6px;height:6px;background:#fff;display:inline-block}
.social .count{height:12px;padding:0 3px;background:#fff;border:1px solid #ccc;color:#333;font-size:6.5px;line-height:10px;border-radius:2px}
.social .btn.alt{background:#0e76a8}
.copyright{left:0;top:1175px;width:760px;height:25px;background:var(--footer-bar);color:var(--footer-text);font-size:8px;text-align:center;line-height:25px}
</style>
</head>
<body>

<header class="abs masthead">
  <svg class="abs masthead-curve" viewBox="0 0 760 80" aria-hidden="true">
    <path d="M0 0 H255 C270 30 280 55 330 70 C280 75 180 80 0 80 Z" fill="#6a0c34" opacity=".45"/>
  </svg>
  <div class="abs brand">
    <span class="brand-dot"></span>
    <div><div class="brand-name">Tallowmere</div><div class="brand-sub">Office Solutions</div></div>
  </div>
  <div class="abs phone-top">
    <svg width="13" height="13" viewBox="0 0 24 24" aria-hidden="true"><path fill="#f5c21b" d="M6.6 10.8a15.1 15.1 0 0 0 6.6 6.6l2.2-2.2c.3-.3.7-.4 1-.2 1.1.4 2.3.6 3.6.6.6 0 1 .4 1 1V20c0 .6-.4 1-1 1A17 17 0 0 1 3 4c0-.6.4-1 1-1h3.5c.6 0 1 .4 1 1 0 1.3.2 2.5.6 3.6.1.3 0 .7-.2 1z"/></svg>
    +91 (44) 55501234
  </div>
  <nav class="abs nav">
    <a class="active">Home</a><a>About us</a><a>Clients</a><a>Services</a><a>Careers</a><a>Current opportunities</a><a>Contact us</a>
  </nav>
  <div class="abs hero" role="img" aria-label="Photo of a vineyard with red grapes, a businessman working on a laptop and wine bottles">
    <div class="abs hero-title">Delivering<br>IT Excellence</div>
    <div class="abs hero-dots"><span class="on"></span><span></span><span></span><span></span><span></span></div>
  </div>
</header>

<section class="abs welcome"></section>
<div class="abs grapes" role="img" aria-label="Illustration of a bunch of grapes"></div>
<h1 class="abs welcome-title">Welcome to <b>Tallowmere Office Solutions</b></h1>
<div class="abs copy welcome-copy">
  <p>An emerging provider of global IT consulting and software services. We are part of the Hollin Cellarhouse group, a family run business and the world's largest multi-channel home delivery wine merchant operating in the UK, USA, Australia, Germany, Hong Kong, Poland and Switzerland.</p>
  <p>Mainly based in the rich cultural city of Chennai in the south east of India, Tallowmere's vision is to deliver outstanding technology solutions to all of the Hollin Cellarhouse group companies that improve business processes, drive efficiencies, support rapid growth and elevate the overall customer experience to a different level.</p>
</div>

<svg class="abs services-tab" viewBox="0 0 215 90" aria-hidden="true">
  <path d="M0 0 H205 C180 20 185 70 140 88 H0 Z" fill="#f3f3f3"/>
</svg>
<h2 class="abs section-title">Our <b>Services</b></h2>
<p class="abs copy services-copy">The services we provide enable the businesses we support to efficiently manage key functions, including order management (encompassing e-commerce websites, inbound and outbound call centre operations), order fulfilment, procurement, planning &amp; forecasting, warehouse management operations, financial management, global compliance and risk management.</p>
<div class="abs tile" style="left:224px;top:680px">Packaged Applications</div>
<div class="abs tile" style="left:456px;top:680px">Enterprise Application Integration</div>
<div class="abs tile" style="left:224px;top:716px">Digital Commerce</div>
<div class="abs tile" style="left:456px;top:716px">Application Development &amp; Maintenance</div>

<section class="abs card" style="left:83px">
  <div class="card-head">Latest Opportunities</div>
  <div class="item" style="top:46px">
    <div class="date">26/11/2013</div>
    <div class="item-title">Software Developers/Programmer Analysts - NX</div>
    <div class="item-text">We are looking for a NX Software Developer to join... <span class="more">[Read More]</span></div>
  </div>
  <div class="divider" style="top:120px"></div>
  <div class="item" style="top:133px">
    <div class="date">26/11/2013</div>
    <div class="item-title">Software Developers/Programmer Analysts - QVM</div>
    <div class="item-text">We are looking for a QVM Software Developer to join... <span class="more">[Read More]</span></div>
  </div>
</section>

<section class="abs card" style="left:291px">
  <div class="card-head">Latest Events</div>
  <div class="thumb" style="top:46px" role="img" aria-label="Event photo of guests tasting wine"></div>
  <div class="event" style="top:46px">
    <div class="date">26/11/2013</div>
    <div class="item-title">Nam nec lorem ipsum</div>
    <div class="item-text">tellus odio ticidunt auctor dosid dolor asis amet... <span class="more">[Read More]</span></div>
  </div>
  <div class="divider" style="top:120px"></div>
  <div class="thumb" style="top:133px" role="img" aria-label="Event photo of guests tasting wine"></div>
  <div class="event" style="top:133px">
    <div class="date">26/11/2013</div>
    <div class="item-title">Nam nec lorem ipsum</div>
    <div class="item-text">tellus odio ticidunt auctor dosid dolor asis amet... <span class="more">[Read More]</span></div>
  </div>
</section>

<section class="abs card" style="left:499px">
  <div class="card-head">Our Clients</div>
  <p class="copy" style="position:absolute;left:9px;top:44px;width:160px">Here are some of the global businesses and brands we support.</p>
  <div class="client-box">Larkspur Wine Club</div>
  <div class="client-link"><i></i>www.larkspurwine.example</div>
  <div class="arrows"><span>‹</span><span>›</span></div>
</section>

<footer class="abs footer">
  <div class="abs foot-col" style="left:83px;top:16px">
    <h4>Quick Links</h4>
    <ul><li>Home</li><li>About us</li><li>Clients</li><li>Services</li><li>Careers</li><li>Current opportunities</li><li>Contact us</li></ul>
  </div>
  <div class="abs foot-col" style="left:211px;top:16px">
    <h4>Our Services</h4>
    <ul><li>Packaged Applications</li><li>Digital Commerce</li><li>Enterprise Application Integration</li><li>Application Development &amp; Maintenance</li></ul>
  </div>
  <div class="abs foot-col" style="left:408px;top:16px">
    <h4>Contact Information</h4>
    <ul class="addr"><li>Tallowmere Office Solutions Pvt. Ltd.</li><li>4th Floor, Meridian Park Tower</li><li>Unit C14 Lakeview Business Estate</li><li>Guindy Chennai, 600099</li><li>Tamil Nadu</li></ul>
    <div class="foot-phone">+91 (44) 55501234</div>
    <div class="foot-mail">contact@tallowmereos.example</div>
  </div>
  <div class="abs foot-col" style="left:596px;top:16px">
    <h4>Social Likes</h4>
    <div class="social"><span class="btn"><i></i>Like</span><span class="count">55</span></div>
    <div class="social"><span class="btn alt"><i></i>Follow</span><span class="count">119</span></div>
  </div>
</footer>
<div class="abs copyright">Copyright© 2014 Tallowmere Office Solutions Pvt. Ltd. All Rights Reserved.</div>

</body>
</html>
```